Bold, Captivating, Passion driven brochure design for an Inspirational Speaker and Trainer

I am looking for a brochure design that will immediately draw people into my energy field. It needs to have bold colors yet soft on the eyes. Placement of information is key. I am a Success Navigator and Inspirational Speaker in need of a brochure design that brings who I am and the value I offer to life... needs to jump right off the page.

Target Market(s)

Small business owners and savvy professionals ages 25-45. I am mainly geared towards the beauty industry because that's where I started; however, I want my materials to help me branch out more beyond the beauty industry.

Contact Information for Business Card

Marla T. Quenby, LLC
Marla T. Quenby
Success Navigator & Inspirational Speaker

Font styles to use
Serif

Requirements
Must have
• Cobalt blue is my favorite color... I would like blues of some kind peppered into the color scheme. Needs to look upscale and seasoned in what I do/offer. Serious and yet inviting - not playful but also not too rigid. Essentially, I don't take myself seriously; however, I take what i do very seriously.
Should not have
• Must not look overdone or inauthentic; not traditional and not overly modernized either

```html
<!DOCTYPE html>
<html lang="en">
<head>
<meta charset="utf-8">
<title>Marla T. Quenby – Excellence Programs</title>
<link rel="stylesheet" href="https://fonts.googleapis.com/css2?family=Alfa+Slab+One&family=Arvo:wght@400;700&family=Fira+Sans:ital,wght@1,700&display=swap">
<style>
  :root{
    --bg-top:#2d4c95;
    --bg-bottom:#3d5eab;
    --panel:#6fa6db;
    --panel-ink:#1c2c66;
    --icon:#a9c3e6;
    --band:#5a8fd0;
    --white:#ffffff;
    --text:#e9effa;
  }
  *{margin:0;padding:0;box-sizing:border-box}
  html,body{width:1200px;height:927px;overflow:hidden}
  body{background:#ffffff}
  .brochure{
    position:relative;width:1200px;height:927px;overflow:hidden;
    background:linear-gradient(160deg,var(--bg-top) 0%,#34549e 55%,var(--bg-bottom) 100%);
    font-family:"Arvo",Georgia,serif;color:var(--text);
  }
  .icon{position:absolute;background:var(--icon);border-radius:14px;opacity:.85}
  .title{
    position:absolute;font-family:"Alfa Slab One",Georgia,serif;color:var(--white);
    font-size:35px;line-height:1.18;font-weight:400;letter-spacing:.5px;
  }
  .panel{
    position:absolute;background:var(--panel);color:var(--panel-ink);
    font-family:"Arvo",Georgia,serif;font-weight:700;font-size:16.5px;line-height:1.3;
    padding:20px 18px;text-align:justify;box-shadow:0 2px 6px rgba(0,0,0,.15);
  }
  .copy{position:absolute;font-size:16px;line-height:1.3;color:var(--text)}
  .copy strong{color:var(--white);font-weight:700}
  .discover-heading{
    position:absolute;left:27px;top:412px;font-family:"Arvo",Georgia,serif;font-weight:700;
    font-size:21px;color:var(--white);transform:rotate(-3deg);
  }
  .discover-list{position:absolute;left:28px;top:452px;width:350px;list-style:none;transform:rotate(-3deg);font-size:16px;line-height:1.3}
  .discover-list li{position:relative;padding-left:22px;margin-bottom:3px}
  .discover-list li::before{content:"";position:absolute;left:2px;top:6px;width:12px;height:12px;border-radius:50%;background:var(--white)}
  .quote{
    position:absolute;font-family:"Fira Sans",Arial,sans-serif;font-style:italic;font-weight:700;
    color:var(--white);font-size:18.5px;line-height:1.3;
  }
  .footer{
    position:absolute;left:0;bottom:0;width:1200px;height:88px;background:var(--band);
    text-align:center;color:var(--white);font-family:"Arvo",Georgia,serif;font-weight:700;
  }
  .footer .cta{font-size:19.5px;padding-top:10px}
  .footer .contact{font-size:19px;padding-top:18px}
</style>
</head>
<body>
<main class="brochure">

  <div class="icon" role="img" aria-label="Icon of a leader raising a hand above a group of people" style="left:22px;top:32px;width:135px;height:100px"></div>
  <h2 class="title" style="left:173px;top:50px">Leadership<br>Excellence</h2>
  <div class="panel" style="left:58px;top:180px;width:318px;height:200px;transform:rotate(5deg)">
    Become the business leader you've always wanted be; one that inspires and empowers greatness in others. Discover the proven strategies used by the greatest business leaders and take your team to the next level in record time.
  </div>
  <h3 class="discover-heading">You will discover:</h3>
  <ul class="discover-list">
    <li>How to effectively communicate your vision</li>
    <li>How to forge a unified purpose</li>
    <li>How to implement an unbreakable system of checks &amp; balances</li>
    <li>How to develop a business culture that everyone envies</li>
    <li>How to become the leader everyone wants to follow</li>
  </ul>
  <p class="quote" style="left:60px;top:700px;width:290px;transform:rotate(4deg)">“If we were a football team Marla would be our head coach. We would have gone to the title game twice now and would have won.”</p>

  <div class="icon" role="img" aria-label="Icon of gears above two people working together" style="left:432px;top:20px;width:130px;height:135px"></div>
  <h2 class="title" style="left:574px;top:28px">Business<br>Culture<br>Excellence</h2>
  <div class="panel" style="left:428px;top:196px;width:296px;height:190px;transform:rotate(-4deg);padding-top:26px">
    Learn Marla's incredible strategies for developing ordinary teams into amazing business cultures that consistently achieve astounding results.
  </div>
  <p class="copy" style="left:425px;top:430px;width:360px;transform:rotate(-1.5deg)">
    Give your team the ultimate edge by delivering the 3 most important <strong>E's</strong> for developing championship teams:<br>
    <strong>1. Engagement</strong> – people commit to and promote what they help create<br>
    <strong>2. Empathy</strong> – they won't care what you know until they know that you care<br>
    <strong>3. Empowerment</strong> – affirm their talents and abilities; hold them accountable
  </p>
  <p class="quote" style="left:432px;top:655px;width:300px;transform:rotate(-4deg)">“Can't even begin to scratch the surface of the gratitude I feel for you my friend. Your workshop and training method are second to none… and I do mean none!”</p>

  <div class="icon" role="img" aria-label="Icon of a businessman beside a dollar sign" style="left:830px;top:40px;width:135px;height:95px"></div>
  <h2 class="title" style="left:983px;top:50px">Sales<br>Excellence</h2>
  <div class="panel" style="left:822px;top:182px;width:334px;height:178px;transform:rotate(5deg)">
    Discover not only how to increase sales but more importantly how to design a sales strategy that continues to generate increased sales and residual revenue over and over again, regardless of the economic climate.
  </div>
  <p class="copy" style="left:825px;top:430px;width:345px;transform:rotate(-1.5deg)">
    You will get the proven strategies on how to bulldoze the <strong>3 main roadblocks</strong> you'll face in sales:<br>
    <strong>1. Trust</strong> – quickly earn the right with even the toughest customers<br>
    <strong>2. Change</strong> – eliminate the fear of change almost immediately<br>
    <strong>3. Value &amp; Convenience</strong> – clearly and succinctly show your customers what's in it for them
  </p>
  <p class="quote" style="left:848px;top:680px;width:285px;transform:rotate(5deg)">“If it weren't for the incredible strategies Marla brings to the table, there's no way I could have grown my business as much as I have… she made the impossible possible.”</p>

  <footer class="footer">
    <p class="cta">Let Marla T. Quenby help you transform your business today! Contact us for your FREE consultation.</p>
    <p class="contact">Office: 555.310.4827 | Mobile: 555.310.9163 | Email: consultation@marlatquenby.com</p>
  </footer>
</main>
</body>
</html>
```